Easy Project! Convert existing logo into Presentation Folder

Our company needs a presentation folder - the type of material you give to a client when they come to your office. It will have pockets for brochures and a spot for a business card.

Existing logos and marketing material are provided as examples. Must also include our Patron Laurel Honour logo. See example for size (9" x 12") at this website: https://www.foldmarkly.ca/search?query=presentation

Target Market(s)

Real Estate Investors

Industry/Entity Type

Real Estate, Property Management

Requirements
Must have
• Logo, Patron Laurel Honour logo, corporate colours. A very "corporate" professional feel, much like a lawyer's office
Nice to have
• Contemporary, elegant design.

```html
<!DOCTYPE html>
<html lang="en">
<head>
<meta charset="utf-8">
<title>Presentation Folder – Inside Spread</title>
<link href="https://fonts.googleapis.com/css2?family=Roboto:wght@400;500;700&display=swap" rel="stylesheet">
<style>
  :root {
    --backdrop: #d9d9da;
    --panel: #f4f4f4;
    --panel-shade: #e4e4e4;
    --spine: #cfcfcf;
    --pocket-light: #0790c9;
    --pocket-dark: #06709f;
    --pocket-edge: #055d85;
    --brand-blue: #1a8fcf;
    --ink: #3a3a3a;
    --card: #ffffff;
  }
  * { margin: 0; padding: 0; box-sizing: border-box; }
  html, body { width: 1200px; height: 847px; overflow: hidden; }
  body {
    background: var(--backdrop);
    font-family: "Roboto", sans-serif;
    position: relative;
  }
  .folder-spread {
    position: absolute;
    left: 0; top: 0;
    width: 1200px; height: 847px;
  }
  .business-card {
    position: absolute;
    left: 768px; top: 552px;
    width: 210px; height: 120px;
    background: var(--card);
    padding: 12px 12px 8px;
    box-shadow: 0 1px 3px rgba(0,0,0,.25);
    color: var(--ink);
    overflow: hidden;
  }
  .card-brand {
    display: flex; align-items: center; gap: 6px;
  }
  .card-brand-mark {
    width: 12px; height: 12px;
    background: var(--brand-blue);
    flex: none;
  }
  .card-brand-name {
    font-size: 9px; font-weight: 500;
    color: var(--brand-blue);
    letter-spacing: .6px;
    line-height: 1.15;
    text-transform: uppercase;
  }
  .card-rule {
    margin: 18px 0 5px;
    border: 0;
    border-top: 1px solid var(--brand-blue);
  }
  .card-name {
    font-size: 7.5px; font-weight: 700;
    color: var(--brand-blue);
    text-transform: uppercase;
  }
  .card-title { font-size: 6px; margin-bottom: 4px; }
  .card-line {
    font-size: 5.4px; line-height: 8px;
    display: flex; align-items: center; gap: 3px;
    white-space: nowrap;
  }
  .card-icon {
    width: 6px; height: 6px; border-radius: 50%;
    border: 1px solid var(--brand-blue);
    flex: none;
  }
  .card-sep { color: var(--brand-blue); padding: 0 2px; }
</style>
</head>
<body>
  <svg class="folder-spread" viewBox="0 0 1200 847" aria-label="Presentation folder inside spread">
    <defs>
      <linearGradient id="panelLeft" x1="0" x2="1" y1="0" y2="0">
        <stop offset="0" stop-color="var(--panel-shade)"/>
        <stop offset="1" stop-color="var(--panel)"/>
      </linearGradient>
      <linearGradient id="panelRight" x1="0" x2="1" y1="0" y2="0">
        <stop offset="0" stop-color="var(--panel-shade)"/>
        <stop offset=".3" stop-color="var(--panel)"/>
        <stop offset="1" stop-color="#fafafa"/>
      </linearGradient>
      <linearGradient id="pocketFill" x1="0" x2="1" y1="0" y2="0">
        <stop offset="0" stop-color="var(--pocket-dark)"/>
        <stop offset="1" stop-color="var(--pocket-light)"/>
      </linearGradient>
    </defs>

    <rect class="panel panel-left" x="55" y="62" width="540" height="720" fill="url(#panelLeft)"/>
    <rect class="spine" x="595" y="62" width="10" height="720" fill="var(--spine)"/>
    <rect class="panel panel-right" x="605" y="62" width="540" height="720" fill="url(#panelRight)"/>

    <path class="pocket pocket-left"
          d="M55 600 C230 548 420 508 570 498 Q590 497 592 512 L592 782 L55 782 Z"
          fill="url(#pocketFill)"/>
    <path class="pocket pocket-right"
          d="M608 782 L608 525 Q610 508 630 504 C820 478 990 468 1145 462 L1145 782 Z"
          fill="url(#pocketFill)"/>

    <g class="card-slits" stroke="var(--pocket-edge)" stroke-width="2" stroke-linecap="round">
      <line x1="764" y1="570" x2="784" y2="548"/>
      <line x1="962" y1="676" x2="982" y2="654"/>
    </g>
  </svg>

  <div class="business-card">
    <div class="card-brand">
      <span class="card-brand-mark"></span>
      <span class="card-brand-name">Summit Ridge<br>Property Management</span>
    </div>
    <hr class="card-rule">
    <div class="card-name">Darren Lowe</div>
    <div class="card-title">President</div>
    <div class="card-line"><span class="card-icon"></span>555-301-0142<span class="card-sep">|</span><span class="card-icon"></span>555-301-0187<span class="card-sep">|</span><span class="card-icon"></span>1-888-555-0163</div>
    <div class="card-line"><span class="card-icon"></span>darren.lowe@summitridgeproperty.ca</div>
    <div class="card-line"><span class="card-icon"></span>B-214 Alder Crest Blvd, Larchmere, Ontario K0L 5B3</div>
  </div>
</body>
</html>
```